Technical Redesign of AI-Generated Method & Topic Graphics for PowerPoint

e have a set of graphics and diagrams that were initially created using AI. The content, structure, and overall layout are already defined and should remain largely unchanged.

The objective is NOT to create completely new designs. This is primarily a technical refinement and conversion project. The graphics need to be professionally redrawn, cleaned up, and rebuilt so that they:

• Look less AI-generated and more professional/corporate
• Match our existing corporate website style
• Are fully editable in Microsoft PowerPoint
• Use consistent fonts, colors, spacing, and iconography
• Maintain the original meaning and information structure

REFERENCE WEBSITE
https://moorwald-forschung. at/

Please use the website as the primary reference for:
• Color palette
• Typography
• Visual language
• General corporate look and feel
• Professional, research-oriented appearance

The style should be clean, technical, modern, and suitable for a scientific/research institution.

SCOPE OF WORK
For each supplied graphic:

1. Recreate the graphic manually
- Do not simply trace or export the AI image.
- Rebuild all elements using PowerPoint native objects where possible.

2. Improve visual quality
- Remove typical AI-generated inconsistencies.
- Correct alignment, spacing, proportions, and visual hierarchy.
- Standardize icons and graphic elements.

3. Corporate style adaptation
- Apply colors and typography consistent with our website.
- Use a professional and technically oriented visual style.
- Avoid decorative or overly creative design elements.

4. Ensure full editability
- All text must remain editable.
- Shapes should be editable PowerPoint objects.
- Icons should preferably be vector-based.
- Elements should not be flattened into images unless absolutely necessary.

DELIVERABLES
Required output:

• Microsoft PowerPoint (.pptx)
• All graphics fully editable
• Layered and logically grouped objects
• Consistent formatting across all graphics
• Optional source files (.svg, .ai, or . eps) if available

DESIGN DIRECTION
Please focus on:

• Technical accuracy
• Professional presentation quality
• Corporate consistency
• PowerPoint usability

Please do NOT focus on:
• Creating alternative concepts
• Artistic reinterpretations
• Major layout changes
• Creative redesigns

The goal is to transform existing AI-generated diagrams into professional, corporate-standard, PowerPoint-editable graphics that fit seamlessly with the Moorwaldinstitut Graz website and presentation materials.

```html
<!DOCTYPE html>
<html lang="en">
<head>
<meta charset="utf-8">
<title>Socio-economic &amp; Socio-technical Analyses</title>
<link href="https://fonts.googleapis.com/css2?family=Nunito+Sans:wght@400;600;700;800&display=swap" rel="stylesheet">
<style>
  :root {
    --green-dark: #4b6b1b;
    --green: #5f7f24;
    --green-soft: #9bb05f;
    --line: #a9b98a;
    --text: #3f4244;
    --text-soft: #55595c;
    --bg: #ffffff;
    --panel-shadow: rgba(60, 70, 40, 0.12);
  }
  * { box-sizing: border-box; margin: 0; padding: 0; }
  html, body { width: 1200px; height: 675px; overflow: hidden; background: var(--bg); }
  body { font-family: "Nunito Sans", Arial, sans-serif; color: var(--text); }
  .slide { position: relative; width: 1200px; height: 675px; background: var(--bg); overflow: hidden; }
  .abs { position: absolute; }

  .slide-title { left: 0; width: 1222px; top: 8px; text-align: center; font-size: 28px; font-weight: 800; color: var(--green-dark); letter-spacing: 0.6px; }
  .slide-subtitle { left: 0; width: 1200px; top: 51px; text-align: center; font-size: 11.5px; line-height: 14.5px; color: var(--text-soft); }

  .soft-panel { background: #fff; border-radius: 14px; box-shadow: 0 1px 8px var(--panel-shadow); }
  .start-panel { left: 116px; top: 95px; width: 187px; height: 98px; }
  .start-panel svg { position: absolute; left: 10px; top: 32px; }
  .start-title { position: absolute; left: 65px; top: 16px; font-size: 12.5px; font-weight: 800; color: var(--green); }
  .start-text { position: absolute; left: 65px; top: 36px; width: 120px; font-size: 8px; line-height: 12px; color: var(--text); }

  .accompany-panel { left: 892px; top: 95px; width: 186px; height: 98px; text-align: center; }
  .accompany-title { margin-top: 12px; font-size: 12px; line-height: 15.5px; font-weight: 800; color: var(--green); }
  .accompany-text { margin-top: 14px; font-size: 8px; line-height: 12px; color: var(--text-soft); }

  .flow-arrow { left: 316px; top: 130px; }
  .process-line { left: 377px; top: 140px; width: 467px; height: 0; border-top: 1px dotted var(--line); }
  .step { top: 116px; width: 100px; margin-left: -50px; text-align: center; }
  .step-icon { width: 48px; height: 48px; margin: 0 auto; border: 1px solid var(--green-soft); border-radius: 50%; background: #fff; display: flex; align-items: center; justify-content: center; }
  .step-label { margin-top: 10px; font-size: 8px; line-height: 11px; color: var(--text); }

  .method-card { top: 219px; height: 176px; border: 1px solid var(--line); border-radius: 9px; background: #fff; }
  .card-title { position: absolute; left: 0; right: 0; top: 10px; text-align: center; font-size: 12.5px; line-height: 17px; font-weight: 700; color: var(--green-dark); }
  .card-icon { position: absolute; }
  .card-list { position: absolute; list-style: none; font-size: 9.5px; line-height: 13.8px; color: var(--text); }
  .card-list li { position: relative; padding-left: 11px; }
  .card-list li::before { content: ""; position: absolute; left: 0; top: 5px; width: 3.5px; height: 3.5px; border-radius: 50%; background: var(--text); }
  .card-list.loose { line-height: 16px; }

  .down-arrow { top: 404px; }

  .insights-panel { left: 114px; top: 431px; width: 968px; height: 157px; border: 1px solid var(--line); border-radius: 9px; background: #fff; }
  .earth-care-mark { left: 153px; top: 450px; width: 116px; height: 118px; border-radius: 50%; border: 1px solid var(--green-soft); background: radial-gradient(circle at 50% 45%, #dfe7cc 0%, #c6d4a2 55%, #eef2e4 100%); }
  .insights-title { left: 114px; width: 968px; top: 441px; padding-left: 80px; text-align: center; font-size: 17px; font-weight: 700; color: var(--green-dark); letter-spacing: 0.3px; }
  .insights-sub { left: 114px; width: 968px; top: 465px; padding-left: 80px; text-align: center; font-size: 11px; color: var(--text); }
  .benefit { display: flex; align-items: center; gap: 12px; height: 24px; font-size: 9px; line-height: 12px; color: var(--text); white-space: nowrap; }
  .benefit svg { flex: none; }
  .row-1 { top: 498px; }
  .row-2 { top: 542px; }
  .col-divider { top: 500px; width: 0; height: 68px; border-left: 1px solid var(--line); }

  .footer-line { top: 635px; height: 0; border-top: 1px solid var(--line); }
  .footer-globe { left: 320px; top: 624px; }
  .footer-text { left: 357px; top: 627px; font-size: 11px; color: var(--text); }
  .brand { left: 1012px; top: 624px; display: flex; align-items: center; gap: 6px; font-size: 12px; font-weight: 800; color: var(--green); }
  .brand-dot { width: 16px; height: 16px; border-radius: 50%; border: 1.5px solid var(--green-soft); }

  .corner-shape { left: 0; top: 560px; }
</style>
</head>
<body>
<div class="slide">

  <svg class="abs corner-shape" width="140" height="115" viewBox="0 0 140 115" aria-hidden="true">
    <path d="M0 36 L28 15 Q40 7 50 18 L138 115 L0 115 Z" fill="var(--green-soft)"/>
  </svg>

  <h1 class="abs slide-title">Socio-economic &amp; Socio-technical Analyses</h1>
  <p class="abs slide-subtitle">Empirical, interdisciplinary insights for sustainable innovation and transformation<br>Methodological Foundations</p>

  <section class="abs soft-panel start-panel">
    <svg width="48" height="48" viewBox="0 0 48 48" fill="none" stroke="var(--green)" stroke-width="1.6" aria-hidden="true">
      <circle cx="20" cy="26" r="18"/><circle cx="20" cy="26" r="12"/><circle cx="20" cy="26" r="6"/>
      <path d="M20 26 L40 6"/><path d="M34 4 L36 10 L42 12"/>
    </svg>
    <h2 class="start-title">Starting Point</h2>
    <p class="start-text">New technologies, products, processes and services Societal, market and policy context</p>
  </section>

  <svg class="abs flow-arrow" width="18" height="22" viewBox="0 0 18 22" aria-hidden="true">
    <path d="M0 6 H8 V0 L18 11 L8 22 V16 H0 Z" fill="var(--green)"/>
  </svg>

  <div class="abs process-line"></div>

  <div class="abs step" style="left:377px">
    <div class="step-icon"><svg width="24" height="24" viewBox="0 0 24 24" fill="none" stroke="var(--green)" stroke-width="1.3"><path d="M6 2 H15 L19 6 V22 H6 Z"/><path d="M9 9 H16 M9 12 H16 M9 15 H16 M9 18 H14"/></svg></div>
    <p class="step-label">Research design &amp;<br>target definition</p>
  </div>
  <div class="abs step" style="left:471px">
    <div class="step-icon"><svg width="26" height="24" viewBox="0 0 26 24" fill="none" stroke="var(--green)" stroke-width="1.3"><circle cx="13" cy="8" r="3"/><circle cx="6" cy="10" r="2.5"/><circle cx="20" cy="10" r="2.5"/><path d="M8 19 Q13 11 18 19 M2 19 Q5 13 9 15 M24 19 Q21 13 17 15"/></svg></div>
    <p class="step-label">Surveys &amp; mixed<br>methods</p>
  </div>
  <div class="abs step" style="left:560px">
    <div class="step-icon"><svg width="24" height="24" viewBox="0 0 24 24" fill="none" stroke="var(--green)" stroke-width="1.3"><path d="M12 3 C18 3 22 6.5 22 11 C22 15.5 18 19 12 19 L6 22 L7 17.5 C3.5 16 2 13.5 2 11 C2 6.5 6 3 12 3 Z"/><circle cx="8" cy="11" r="0.8" fill="var(--green)"/><circle cx="12" cy="11" r="0.8" fill="var(--green)"/><circle cx="16" cy="11" r="0.8" fill="var(--green)"/></svg></div>
    <p class="step-label">Qualitative &amp;<br>quantitative data</p>
  </div>
  <div class="abs step" style="left:654px">
    <div class="step-icon"><svg width="24" height="24" viewBox="0 0 24 24" fill="none" stroke="var(--green)" stroke-width="1.3"><rect x="3" y="15" width="3.5" height="6"/><rect x="8.5" y="11" width="3.5" height="10"/><rect x="14" y="7" width="3.5" height="14"/><rect x="19.5" y="3" width="2.5" height="18"/></svg></div>
    <p class="step-label">Empirical analysis &amp;<br>interpretation</p>
  </div>
  <div class="abs step" style="left:750px">
    <div class="step-icon"><svg width="24" height="24" viewBox="0 0 24 24" fill="none" stroke="var(--green)" stroke-width="1.3"><path d="M19 6 A8 8 0 1 0 19 18"/><path d="M4 10 H14 M4 14 H14"/></svg></div>
    <p class="step-label">Economic &amp; market<br>perspectives</p>
  </div>
  <div class="abs step" style="left:844px">
    <div class="step-icon"><svg width="24" height="24" viewBox="0 0 24 24" fill="none" stroke="var(--green)" stroke-width="1.4"><circle cx="14" cy="9" r="6.5"/><path d="M9.5 14 L3 21"/></svg></div>
    <p class="step-label">Scenarios &amp;<br>sensitivities</p>
  </div>

  <section class="abs soft-panel accompany-panel">
    <h2 class="accompany-title">Accompanying Innovation<br>&amp; Transformation</h2>
    <p class="accompany-text">Insights for early development<br>and implementation phases</p>
  </section>

  <section class="abs method-card" style="left:114px;width:237px">
    <h3 class="card-title">Surveys &amp; Data<br>Collection</h3>
    <svg class="card-icon" style="left:24px;top:50px" width="46" height="62" viewBox="0 0 46 62" fill="none" stroke="var(--green-dark)" stroke-width="2.4">
      <rect x="3" y="6" width="40" height="54" rx="3"/><rect x="15" y="2" width="16" height="7" rx="2"/>
      <path d="M9 20 L12 23 L16 18 M9 31 L12 34 L16 29 M9 42 L12 45 L16 40 M9 52 L12 55 L16 50"/>
      <path d="M21 21 H37 M21 32 H37 M21 43 H37 M21 53 H37"/>
    </svg>
    <ul class="card-list" style="left:91px;top:58px;width:140px">
      <li>Stakeholder and citizen surveys</li>
      <li>Attitudes, acceptance,</li>
      <li>behavior and preferences</li>
      <li>Context and trend information</li>
    </ul>
  </section>

  <section class="abs method-card" style="left:361px;width:232px">
    <h3 class="card-title" style="top:11px">Expert Knowledge &amp;<br>Interviews</h3>
    <div class="card-icon" role="img" aria-label="Illustration of two experts talking at a table" style="left:10px;top:64px;width:58px;height:42px;border-radius:6px;background:linear-gradient(180deg,#7d9643,#5f7f24)"></div>
    <ul class="card-list" style="left:83px;top:58px;width:140px">
      <li>Interviews with experts and key actors</li>
      <li>Multiple perspectives from practice and research</li>
      <li>Basis for informed assessments</li>
    </ul>
  </section>

  <section class="abs method-card" style="left:604px;width:236px">
    <h3 class="card-title" style="color:var(--green)">Market &amp; Innovation<br>Analysis</h3>
    <svg class="card-icon" style="left:13px;top:64px" width="46" height="46" viewBox="0 0 46 46" fill="none" stroke="var(--green-dark)" stroke-width="3">
      <circle cx="19" cy="19" r="15"/><path d="M30 30 L43 43" stroke-linecap="round" stroke-width="4"/>
      <path d="M12 26 V21 M17 26 V18 M22 26 V14 M27 26 V11" stroke-width="3.2"/>
    </svg>
    <ul class="card-list loose" style="left:80px;top:57px;width:150px">
      <li>Market potential and adoption drivers</li>
      <li>Willingness-to-pay and value perception</li>
      <li>Policy and business implications</li>
    </ul>
  </section>

  <section class="abs method-card" style="left:851px;width:231px">
    <h3 class="card-title" style="top:11px">Barriers, Opportunities &amp;<br>Recommendations</h3>
    <svg class="card-icon" style="left:12px;top:60px" width="42" height="56" viewBox="0 0 42 56" fill="var(--green-dark)">
      <rect x="18" y="2" width="5" height="52"/><rect x="6" y="53" width="30" height="3"/>
      <path d="M2 8 H34 L40 14 L34 20 H2 Z"/><path d="M8 24 H40 V36 H8 L2 30 Z"/>
    </svg>
    <ul class="card-list" style="left:70px;top:58px;width:155px">
      <li>Identification of barriers and enablers</li>
      <li>Strategic and policy recommendations</li>
      <li>Measures for successful implementation</li>
    </ul>
  </section>

  <svg class="abs down-arrow" style="left:227px" width="10" height="16" viewBox="0 0 10 16" aria-hidden="true"><path d="M5 0 V14 M1 10 L5 15 L9 10" stroke="var(--green-dark)" stroke-width="1.6" fill="none"/></svg>
  <svg class="abs down-arrow" style="left:472px" width="10" height="16" viewBox="0 0 10 16" aria-hidden="true"><path d="M5 0 V14 M1 10 L5 15 L9 10" stroke="var(--green-dark)" stroke-width="1.6" fill="none"/></svg>
  <svg class="abs down-arrow" style="left:716px" width="10" height="16" viewBox="0 0 10 16" aria-hidden="true"><path d="M5 0 V14 M1 10 L5 15 L9 10" stroke="var(--green-dark)" stroke-width="1.6" fill="none"/></svg>
  <svg class="abs down-arrow" style="left:962px" width="10" height="16" viewBox="0 0 10 16" aria-hidden="true"><path d="M5 0 V14 M1 10 L5 15 L9 10" stroke="var(--green-dark)" stroke-width="1.6" fill="none"/></svg>

  <section class="abs insights-panel"></section>
  <div class="abs earth-care-mark" role="img" aria-label="Illustration of a hand holding the globe with a leaf"></div>
  <h2 class="abs insights-title">Integrated Insights for Better Decisions</h2>
  <p class="abs insights-sub">Empirically grounded, interdisciplinary analysis for sustainable impact</p>

  <div class="abs benefit row-1" style="left:319px"><svg width="21" height="21" viewBox="0 0 22 22" fill="none" stroke="var(--green)" stroke-width="1.3"><circle cx="11" cy="11" r="10"/><path d="M6.5 11 L9.7 14.2 L15.5 7.8"/></svg><span>Deeper understanding of needs,<br>behaviors and acceptance</span></div>
  <div class="abs benefit row-2" style="left:319px"><svg width="21" height="21" viewBox="0 0 22 22" fill="none" stroke="var(--green)" stroke-width="1.3"><circle cx="11" cy="11" r="10"/><path d="M6.5 11 L9.7 14.2 L15.5 7.8"/></svg><span>Sound evidence for strategy<br>and decision-making</span></div>

  <div class="abs col-divider" style="left:518px"></div>

  <div class="abs benefit row-1" style="left:544px"><svg width="21" height="21" viewBox="0 0 22 22" fill="none" stroke="var(--green)" stroke-width="1.3"><circle cx="11" cy="11" r="10"/><path d="M6.5 11 L9.7 14.2 L15.5 7.8"/></svg><span>Early identification of risks,<br>opportunities and trade-offs</span></div>
  <div class="abs benefit row-2" style="left:544px"><svg width="21" height="21" viewBox="0 0 22 22" fill="none" stroke="var(--green)" stroke-width="1.3"><circle cx="11" cy="11" r="10"/><path d="M6.5 11 L9.7 14.2 L15.5 7.8"/></svg><span>Actionable recommendations<br>for innovation and policy</span></div>

  <div class="abs col-divider" style="left:738px"></div>

  <div class="abs benefit row-1" style="left:757px"><svg width="21" height="21" viewBox="0 0 22 22" fill="none" stroke="var(--green)" stroke-width="1.3"><circle cx="11" cy="11" r="10"/><path d="M6.5 11 L9.7 14.2 L15.5 7.8"/></svg><span>Support for sustainable<br>transformation and impact</span></div>
  <div class="abs benefit row-2" style="left:757px"><svg width="21" height="21" viewBox="0 0 22 22" fill="none" stroke="var(--green)" stroke-width="1.3"><circle cx="11" cy="11" r="10"/><path d="M6.5 11 L9.7 14.2 L15.5 7.8"/></svg><span>Stronger alignment of technology,<br>markets and society</span></div>

  <div class="abs footer-line" style="left:113px;width:195px"></div>
  <svg class="abs footer-globe" width="24" height="24" viewBox="0 0 24 24" fill="none" stroke="var(--green)" stroke-width="1.1" aria-hidden="true">
    <circle cx="12" cy="12" r="10.5"/><ellipse cx="12" cy="12" rx="4.5" ry="10.5"/><path d="M1.5 12 H22.5 M3.5 6.5 H20.5 M3.5 17.5 H20.5 M12 1.5 V22.5"/>
  </svg>
  <p class="abs footer-text">Applicable to technologies, services, markets and societal transformation processes</p>
  <div class="abs footer-line" style="left:812px;width:186px"></div>

  <div class="abs brand"><span class="brand-dot"></span>Moorwaldinstitut Graz</div>
</div>
</body>
</html>
```